Ranked amongst the Best Colleges and Programs

the size of the ad is Full Page, with bleed*
8”x 10.75" plus 0.25" bleed'
you have two choices for the tagline .. please chose what ever you think will allow you to make a better ad.
The instructions on the brief are in red
I am looking for a hight quality modern ad to place in local weekly publications that will stand out .
I would like a ad that people will look at and say i would like to see what this ad is all about.
I apprecate creative work.
the ad should not be very crowded and the text should be able to be read.
if you decide to use people in the ad .. (you don't have to ) then it should be a male dressed in white shirt in and sports jacket.. or if you would like you can use a vector and then use male or female people.
please leave one inch on the bottom for the footer

Target Market(s)

potential middle class students from 23-35 years of age

Industry/Entity Type

education

Requirements
Must have
• .the " 98% employment rate" should stand out in the ad.. but should not be the main part of the ad
Nice to have
• creative
Should not have
• Should not be a very busy or crowded ad.. i prefer pictures of men but should be .. in a business suit .. that looks professional- white shirt

```html
<!DOCTYPE html>
<html lang="en">
<head>
<meta charset="utf-8">
<title>HVU Masters of Accounting – Full Page Ad</title>
<link rel="stylesheet" href="https://fonts.googleapis.com/css2?family=Saira+Condensed:wght@600;700;800&family=PT+Sans:wght@400;700&display=swap">
<style>
  :root {
    --sky: #10a0c6;
    --navy: #0a3658;
    --paper: #f3f3f3;
    --footer: #dcdddd;
    --ink: #233546;
    --white: #ffffff;
  }
  * { margin: 0; padding: 0; box-sizing: border-box; }
  html, body { width: 970px; height: 1200px; overflow: hidden; background: var(--paper); }
  .ad { position: relative; width: 970px; height: 1200px; background: var(--paper); overflow: hidden; font-family: "PT Sans", sans-serif; }

  .portrait {
    position: absolute; left: 330px; top: 26px; width: 595px; height: 700px;
    background: radial-gradient(ellipse at 65% 40%, #2a2a2e 0%, #1a1a1d 45%, rgba(243,243,243,0) 72%);
  }

  .headline { position: absolute; left: 67px; top: 118px; width: 400px; font-family: "Saira Condensed", sans-serif; font-weight: 700; text-transform: uppercase; line-height: 1; }
  .headline span { display: block; }
  .headline .sky { color: var(--sky); }
  .headline .navy { color: var(--navy); }
  .line-small { font-size: 100px; letter-spacing: -1px; }
  .line-invest { font-size: 64px; margin-top: 3px; }
  .line-today { font-size: 64px; margin-top: 2px; }
  .right { text-align: right; padding-right: 15px; }
  .line-big { font-size: 88px; margin-top: 4px; }
  .line-diff { font-size: 78px; margin-top: -4px; }
  .line-tomorrow { font-size: 76px; margin-top: -6px; padding-right: 0 !important; }

  .program-tag {
    position: absolute; left: 67px; top: 615px; width: 387px; height: 42px;
    background: var(--navy); color: var(--white); border-radius: 6px;
    font-weight: 700; font-size: 23px; line-height: 42px; text-align: center;
  }

  .bands { position: absolute; left: 0; top: 0; width: 970px; height: 1200px; }

  .rankings { position: absolute; left: 70px; top: 856px; color: var(--white); }
  .rankings h2 { font-size: 36px; font-weight: 700; margin-bottom: 14px; }
  .rankings p { font-size: 22px; color: var(--ink); line-height: 1.3; margin-bottom: 6px; }
  .rankings b { font-weight: 700; }

  .stat { position: absolute; left: 500px; top: 700px; }
  .stat-figure { font-family: "Saira Condensed", sans-serif; font-weight: 800; color: var(--navy); font-size: 112px; line-height: 1; margin-left: 46px; letter-spacing: -2px; }
  .stat-figure small { font-size: 40px; font-weight: 700; letter-spacing: 0; }
  .stat-label { font-family: "Saira Condensed", sans-serif; font-weight: 700; color: var(--white); font-size: 60px; line-height: 1; margin-top: 6px; }
  .stat-note { width: 340px; margin-top: 18px; font-size: 15.5px; line-height: 21px; color: var(--ink); }
</style>
</head>
<body>
<div class="ad">
  <div class="portrait" role="img" aria-label="Photo of a smiling young man in glasses, black suit, white shirt and tie, holding his hands apart as if measuring a size"></div>

  <h1 class="headline">
    <span class="sky line-small">A Small</span>
    <span class="sky line-invest">Investment</span>
    <span class="navy line-today">Today,</span>
    <span class="sky line-big right">A Big</span>
    <span class="sky line-diff right">Difference</span>
    <span class="navy line-tomorrow right">Tomorrow.</span>
  </h1>

  <div class="program-tag">HVU- Masters of Accounting</div>

  <svg class="bands" viewBox="0 0 970 1200" aria-hidden="true">
    <polygon points="0,813 553,706 553,727 0,839" fill="var(--navy)"/>
    <polygon points="0,839 970,643 970,1049 0,1049" fill="var(--sky)"/>
    <rect x="0" y="1049" width="970" height="151" fill="var(--footer)"/>
  </svg>

  <section class="rankings">
    <h2>Ranked amongst:</h2>
    <p><b>Best Colleges -</b> Ledger Review 2023</p>
    <p><b>Best Masters In Accounting -</b><br>Globe Academic 2023</p>
  </section>

  <section class="stat">
    <div class="stat-figure">98<small>%</small></div>
    <div class="stat-label">employment rate</div>
    <p class="stat-note">HVU graduates have gone on to work in various high-quality jobs in top firms, earning impressive six-figure salaries as well as opening successful businesses.</p>
  </section>
</div>
</body>
</html>
```